Walking Faithful Pathways book cover design

Title: Walking Faithful Pathways
Subtitle: How to hear and do the will of God

Ed Brantwell

top of book starburst or graphic: Updated & Expanded!

Design front, back cover and spine

Size: 8 1/2 inches x 5 1/2 inches, color, spine 1/4 inch

Book is about helping Christian understand how to hear God and how to make Godly decisions in life and work.

Target Market(s)

Christian evangelical audience, men and women adults

Colors

Designer to choose colors to be used in the design.

Requirements
Must have
• Open to suggestions
Nice to have
• Open to suggestions

```html
<!DOCTYPE html>
<html lang="en">
<head>
<meta charset="utf-8">
<title>Walking Faithful Pathways – Book Cover</title>
<link rel="stylesheet" href="https://fonts.googleapis.com/css2?family=Cinzel:wght@400;500;600&family=Crimson+Pro:wght@600&family=EB+Garamond:wght@400&display=swap">
<style>
  :root {
    --page: #ffffff;
    --cover-black: #0b0908;
    --navy-glow: #17324d;
    --gold: #f0c24a;
    --gold-deep: #c48a1e;
    --ivory: #f4efe4;
    --body-text: #f2f0ec;
    --rule: #3a3530;
  }
  * { margin: 0; padding: 0; box-sizing: border-box; }
  html, body { width: 1200px; height: 1200px; overflow: hidden; background: var(--page); }
  .canvas { position: relative; width: 1200px; height: 1200px; background: var(--page); }

  .cover-spread {
    position: absolute; left: 0; top: 147px; width: 1200px; height: 906px;
    background: var(--cover-black); overflow: hidden;
  }

  /* Back cover */
  .back-rule { position: absolute; left: 118px; top: 36px; width: 422px; height: 1px; background: var(--rule); }
  .back-photo {
    position: absolute; left: 176px; top: 44px; width: 256px; height: 202px;
    border-radius: 46% 40% 42% 38% / 36% 44% 40% 46%;
    background: radial-gradient(ellipse at 55% 35%, #fffbe8 0%, #f3d98a 22%, #b88a3a 48%, #4a3a26 72%, rgba(11,9,8,0) 100%);
  }
  .back-copy {
    position: absolute; left: 58px; top: 274px; width: 492px;
    font-family: "EB Garamond", Georgia, serif; font-size: 15.6px; line-height: 20.2px;
    color: var(--body-text); text-align: justify; hyphens: auto;
  }
  .back-copy p + p { margin-top: 20px; }

  /* Spine */
  .spine { position: absolute; left: 572px; top: 0; width: 50px; height: 906px; }
  .spine-title, .spine-author {
    position: absolute; left: 50%; transform: translateX(-50%);
    writing-mode: vertical-rl; font-family: "Cinzel", "Times New Roman", serif; white-space: nowrap;
  }
  .spine-title { top: 196px; font-size: 20px; letter-spacing: 3.2px; color: var(--gold); }
  .spine-author { top: 622px; font-size: 22px; letter-spacing: 2px; color: var(--ivory); }

  /* Front cover */
  .front {
    position: absolute; left: 615px; top: 0; width: 585px; height: 906px;
    background: radial-gradient(ellipse 70% 45% at 52% 28%, var(--navy-glow) 0%, #0d1a28 55%, var(--cover-black) 100%);
  }
  .front-photo {
    position: absolute; left: 0; top: 412px; width: 585px; height: 494px;
    background:
      radial-gradient(ellipse 55% 45% at 55% 30%, #fffdf0 0%, #f7e6a6 25%, rgba(214,170,80,0.6) 55%, rgba(0,0,0,0) 80%),
      linear-gradient(180deg, #3a2e24 0%, #7b6a45 40%, #8f7a44 70%, #4e4224 100%);
    border-radius: 18% 14% 0 0 / 12% 10% 0 0;
  }
  .badge { position: absolute; left: 12px; top: 18px; width: 92px; height: 92px; }
  .badge-text {
    position: absolute; left: 12px; top: 18px; width: 92px; height: 92px;
    display: flex; flex-direction: column; align-items: center; justify-content: center;
    transform: rotate(-18deg);
    font-family: "Crimson Pro", Georgia, serif; font-weight: 600; font-size: 10.5px; line-height: 11px;
    color: #2a1a05; text-align: center; letter-spacing: 0.3px;
  }
  .title {
    position: absolute; left: 0; top: 52px; width: 585px; text-align: center;
    font-family: "Cinzel", "Times New Roman", serif; font-weight: 500; color: var(--gold);
    text-shadow: 0 2px 4px rgba(0,0,0,0.6);
  }
  .title span { display: block; }
  .title .line-one { font-size: 62px; line-height: 76px; letter-spacing: 6px; }
  .title .line-two { font-size: 84px; line-height: 104px; letter-spacing: 1px; margin-top: 8px; }
  .title .line-three { font-size: 66px; line-height: 84px; letter-spacing: 3px; margin-top: 10px; }
  .subtitle {
    position: absolute; left: 0; top: 346px; width: 585px; text-align: center;
    font-family: "Crimson Pro", Georgia, serif; font-weight: 600; font-size: 26px; letter-spacing: 0.8px;
    color: var(--ivory);
  }
  .author {
    position: absolute; left: 0; top: 828px; width: 585px; text-align: center;
    font-family: "Cinzel", "Times New Roman", serif; font-size: 40px; letter-spacing: 2px;
    color: var(--ivory); text-shadow: 0 2px 6px rgba(0,0,0,0.7);
  }
</style>
</head>
<body>
<div class="canvas">
  <div class="cover-spread">
    <section class="back">
      <div class="back-rule"></div>
      <div class="back-photo" role="img" aria-label="Photograph: railway tracks seen through a hole in a stone wall toward a bright sunrise"></div>
      <div class="back-copy">
        <p>Lorem ipsum dolor sit amet, consectetur adipiscing elit. Suspendisse lacinia dictum risus id bibendum. In vehicula, sem sit amet tempus eleifend, tellus nisl eleifend sapien, a tempor turpis est mattis sem. In fringilla orci ac metus dictum molestie. Sed dapibus fermentum felis, et pellentesque neque venenatis vel. Donec quis pharetra ex, et ullamcorper sapien. Pellentesque massa tellus, ornare a porta vel, eleifend in metus. Fusce consectetur ante interdum est aliquam semper. Sed ex neque, maximus quis urna et, fringilla facilisis ante. Fusce nec vulputate neque. Sed blandit neque at tortor vulputate rhoncus. Aenean accumsan neque sit amet orci bibendum finibus. Vestibulum porta facilisis ante sit amet rutrum.</p>
        <p>Vivamus rhoncus ex at efficitur facilisis. Curabitur nec lobortis lorem, eu sagittis lorem. Suspendisse et feugiat augue. Quisque odio elit, commodo sed odio a, luctus commodo diam. Sed a fermentum ipsum, ac porttitor purus. Aenean convallis sem et sollicitudin lacinia. Aliquam erat volutpat. Praesent blandit ut lorem feugiat tristique. Nunc ut ullamcorper enim. Nunc porta elit id tellus sollicitudin, in dictum mauris porta. Vestibulum posuere porttitor nunc tincidunt tincidunt.</p>
        <p>Integer pharetra ultrices velit, vel lobortis diam rhoncus eu. Cras porttitor</p>
      </div>
    </section>

    <section class="spine">
      <div class="spine-title">WALKING FAITHFUL PATHWAYS</div>
      <div class="spine-author">ED BRANTWELL</div>
    </section>

    <section class="front">
      <div class="front-photo" role="img" aria-label="Photograph: broken stone wall opening onto railway tracks leading into golden sunlight"></div>
      <svg class="badge" viewBox="0 0 92 92" aria-hidden="true">
        <defs>
          <radialGradient id="badgeGold" cx="40%" cy="35%" r="70%">
            <stop offset="0%" stop-color="#ffe58a"/>
            <stop offset="60%" stop-color="#e0a92f"/>
            <stop offset="100%" stop-color="#a8701a"/>
          </radialGradient>
        </defs>
        <polygon fill="url(#badgeGold)" points="46,1 52,8 60,3 64,11 73,9 75,18 84,19 83,28 91,32 87,40 92,46 87,52 91,60 83,64 84,73 75,74 73,83 64,81 60,89 52,84 46,91 40,84 32,89 28,81 19,83 17,74 8,73 9,64 1,60 5,52 0,46 5,40 1,32 9,28 8,19 17,18 19,9 28,11 32,3 40,8"/>
        <circle cx="46" cy="46" r="34" fill="none" stroke="#fff1b8" stroke-opacity="0.6" stroke-width="1"/>
      </svg>
      <div class="badge-text"><span>UPDATED</span><span>&amp;</span><span>EXPANDED!</span></div>

      <h1 class="title">
        <span class="line-one">WALKING</span>
        <span class="line-two">FAITHFUL</span>
        <span class="line-three">PATHWAYS</span>
      </h1>
      <p class="subtitle">How to hear and do the will of God</p>
      <p class="author">Ed Brantwell</p>
    </section>
  </div>
</div>
</body>
</html>
```